LumeWear e-commerce website design for cartwell platform

I currently have a trendy e-commerce clothing store that is primarily based off of the Southern California Style/Trends. I am looking for a redesign of my cartwell template as I don't like my current image. I am looking for a sleek clean design that allows more focus on the products. I like neutral backgrounds and easy to use websites. Should be responsive to mobile devices. I would also like to have some ideas for a slide show picture that notifies customers of free shipping if possible. I do also have a theme template that I purchased through Cartwell so one could set the theme up for me and edit it to what I need. My website is lumewear.example if you would like to look at the type of products I have. I am also looking to do a logo redesign as well- looking for a more stylish logo that would appeal to an approximate age range of 18-40 year old women. I want to be remembered, something to match the web design.

I like teal/turquoise and grey combos but I don't have to have this as the colors.

Target Market(s)

approx. 18-40

Industry/Entity Type

E-Commerce

Number of Pages Required

2 page

Requirements
Must have
• Menu bar, cartwell compatible, easy to access/navigate, responsive to mobile devices, easy product upload
Nice to have
• if able ability to resize pictures all to the same size
Should not have
• not be difficult to navigate both on a reg. computer or mobile device

```html
<!DOCTYPE html>
<html lang="en">
<head>
<meta charset="utf-8">
<title>LumeWear – Home</title>
<link href="https://fonts.googleapis.com/css2?family=Montserrat:wght@400;600;700;800&family=Pacifico&display=swap" rel="stylesheet">
<style>
:root{
  --pink:#ef8fa6;
  --pink-soft:#f6c3cf;
  --pink-pale:#fbe6eb;
  --ink:#3a3a3a;
  --muted:#8c8c8c;
  --line:#e4e4e4;
  --white:#ffffff;
  --backdrop-a:#f6e4e6;
  --backdrop-b:#eef0e4;
  --hero-bg:#ecebea;
  --promo-mint:#d9efe8;
  --promo-blush:#f3d6dd;
  --product-bg:#f4f4f4;
}
*{box-sizing:border-box;margin:0;padding:0}
html,body{width:809px;height:1200px;overflow:hidden}
body{font-family:"Montserrat",sans-serif;color:var(--ink);position:relative}
.backdrop{position:absolute;inset:0;background:linear-gradient(135deg,var(--backdrop-a),var(--backdrop-b) 50%,var(--backdrop-a))}
.page{position:absolute;left:89px;top:28px;width:631px;height:1146px;background:var(--white);padding:0 11px}
.header{height:62px;display:flex;align-items:center;justify-content:space-between}
.logo{display:flex;align-items:center;gap:8px;font-weight:800;font-size:22px;color:var(--ink)}
.logo-dot{width:12px;height:12px;border-radius:50%;background:var(--pink)}
.cart{display:flex;align-items:center;gap:8px;font-size:9px;text-align:right;line-height:1.3}
.cart small{color:var(--muted);display:block}
.cart-icon{width:24px;height:24px;border-radius:50%;background:var(--pink);display:flex;align-items:center;justify-content:center}
.nav{height:30px;display:flex;align-items:center;border-bottom:1px solid var(--line);font-size:9px;font-weight:600}
.nav a{color:var(--ink);text-decoration:none;margin-right:18px}
.nav .account{margin-left:auto;display:flex;gap:12px;font-weight:400;color:var(--muted)}
.hero{position:relative;margin-top:16px;height:222px;background:linear-gradient(90deg,var(--hero-bg),#f7f3f0)}
.hero-photo{position:absolute;right:0;top:0;width:330px;height:100%;background:linear-gradient(160deg,#f28a6a,#e9a98e 45%,#6f89a8)}
.hero-copy{position:absolute;left:130px;top:42px;text-align:center}
.hero-script{font-family:"Pacifico",cursive;font-size:18px;color:var(--ink)}
.hero-title{font-size:36px;font-weight:800;color:var(--pink);line-height:1}
.hero-sub{font-size:11px;letter-spacing:2px;margin-top:6px}
.btn{display:inline-block;background:var(--pink);color:var(--white);font-size:8px;font-weight:700;letter-spacing:1px;padding:5px 14px;margin-top:14px}
.arrow{position:absolute;top:96px;width:14px;height:30px;background:var(--white);display:flex;align-items:center;justify-content:center}
.arrow.left{left:0}.arrow.right{right:0}
.promos{display:flex;gap:10px;margin-top:14px;height:128px}
.promo{position:relative;flex:1}
.promo-mint{background:linear-gradient(90deg,var(--promo-mint),#bfe1d8)}
.promo-gift{background:linear-gradient(135deg,#fafafa,var(--pink-pale))}
.promo-blush{background:var(--promo-blush)}
.promo-tag{position:absolute;right:14px;top:36px;width:62px;height:62px;border-radius:50%;background:var(--white);text-align:center;padding-top:14px;font-family:"Pacifico",cursive;font-size:11px;color:var(--pink);line-height:1.1}
.promo-tag small{display:block;font-family:"Montserrat",sans-serif;font-size:6px;color:var(--ink);margin-top:2px}
.free{position:absolute;inset:0;display:flex;align-items:center;justify-content:center;text-align:center;font-family:"Pacifico",cursive;font-size:24px;color:var(--white);line-height:1.2}
.products{display:grid;grid-template-columns:repeat(3,1fr);gap:12px 14px;margin-top:14px;border-top:1px solid var(--line);padding-top:12px}
.product{position:relative;text-align:center}
.product-photo{height:182px;background:var(--product-bg)}
.ph-blue{background:linear-gradient(180deg,var(--product-bg),#3a55c4 40%,#2f47a8 80%,var(--product-bg))}
.ph-grey{background:linear-gradient(180deg,var(--product-bg),#8a8a8a 40%,#2e2e2e 85%,var(--product-bg))}
.ph-pink{background:linear-gradient(180deg,var(--product-bg),#ead8c6 40%,#ee89a4 75%,var(--product-bg))}
.ribbon{position:absolute;left:0;top:0;width:0;height:0;border-top:28px solid #8fd0b8;border-right:28px solid transparent}
.product-name{font-size:7px;font-weight:600;letter-spacing:1px;margin-top:8px}
.price{font-size:14px;font-weight:700;margin-top:2px}
.product .btn{margin-top:4px;padding:4px 10px;font-size:7px}
.footer{position:absolute;left:11px;right:11px;top:1030px;border-top:1px solid var(--line);padding-top:12px;text-align:center}
.payments{display:flex;justify-content:center;align-items:center;gap:5px;font-size:7px;color:var(--muted)}
.card{width:22px;height:14px;border-radius:2px;background:#c9ccd4}
.social{display:flex;justify-content:center;gap:8px;margin-top:14px}
.social span{width:18px;height:18px;border-radius:50%;background:#6b9bd1}
.social span:nth-child(2){background:#cf4c5c}
.social span:nth-child(3){background:#3f5f9e}
.copy{font-size:7px;color:var(--muted);margin-top:10px}
</style>
</head>
<body>
<div class="backdrop" role="img" aria-label="Soft floral pattern background with pink roses"></div>
<main class="page">
  <header class="header">
    <div class="logo"><span class="logo-dot"></span>LumeWear</div>
    <div class="cart"><div>Your cart<small>0 items</small></div>
      <span class="cart-icon"><svg width="12" height="12" viewBox="0 0 12 12"><path d="M2 4h8l-1 7H3z" fill="none" stroke="#fff" stroke-width="1.2"/><path d="M4 4a2 2 0 0 1 4 0" fill="none" stroke="#fff" stroke-width="1.2"/></svg></span>
    </div>
  </header>
  <nav class="nav">
    <a href="#">What's New?</a><a href="#">Dresses</a><a href="#">Tops</a><a href="#">Bottoms/Rompers</a><a href="#">Accessories</a><a href="#">Sale</a><a href="#">A little about us</a>
    <span class="account"><span>Check account</span><span>Login</span></span>
  </nav>
  <section class="hero">
    <div class="hero-photo" role="img" aria-label="Model in a coral top and denim shorts"></div>
    <div class="hero-copy">
      <div class="hero-script">Crazy</div>
      <div class="hero-title">CRAZY<br>SUMMER</div>
      <div class="hero-sub">WOMAN COLLECTION</div>
      <span class="btn">SHOP NOW</span>
    </div>
    <span class="arrow left"><svg width="6" height="10"><path d="M5 1 1 5l4 4" fill="none" stroke="#999"/></svg></span>
    <span class="arrow right"><svg width="6" height="10"><path d="M1 1l4 4-4 4" fill="none" stroke="#999"/></svg></span>
  </section>
  <section class="promos">
    <div class="promo promo-mint" role="img" aria-label="Model in a mint top on the beach">
      <div class="promo-tag">Summer Party<small>COLLECTION</small></div>
    </div>
    <div class="promo promo-gift" role="img" aria-label="Gift tags tied with pink ribbon"></div>
    <div class="promo promo-blush"><div class="free">Free<br>Shipping</div></div>
  </section>
  <section class="products">
    <article class="product"><div class="product-photo ph-blue" role="img" aria-label="Blue tank dress"></div><div class="product-name">TANK DRESS</div><div class="price">$64.95</div><span class="btn">ADD TO CART</span></article>
    <article class="product"><div class="product-photo ph-grey" role="img" aria-label="Grey top with black shorts"></div><span class="ribbon"></span><div class="product-name">TANK DRESS</div><div class="price">$64.95</div><span class="btn">ADD TO CART</span></article>
    <article class="product"><div class="product-photo ph-pink" role="img" aria-label="Patterned top with pink floral shorts"></div><div class="product-name">TANK DRESS</div><div class="price">$64.95</div><span class="btn">ADD TO CART</span></article>
    <article class="product"><div class="product-photo ph-blue" role="img" aria-label="Blue tank dress"></div><div class="product-name">TANK DRESS</div><div class="price">$64.95</div><span class="btn">ADD TO CART</span></article>
    <article class="product"><div class="product-photo ph-grey" role="img" aria-label="Grey top with black shorts"></div><span class="ribbon"></span><div class="product-name">TANK DRESS</div><div class="price">$64.95</div><span class="btn">ADD TO CART</span></article>
    <article class="product"><div class="product-photo ph-pink" role="img" aria-label="Patterned top with pink floral shorts"></div><div class="product-name">TANK DRESS</div><div class="price">$64.95</div><span class="btn">ADD TO CART</span></article>
  </section>
  <footer class="footer">
    <div class="payments">We accept <span class="card"></span><span class="card"></span><span class="card"></span><span class="card"></span><span class="card"></span><span class="card"></span><span class="card"></span><span class="card"></span><span class="card"></span><span class="card"></span><span class="card"></span><span class="card"></span></div>
    <div class="social"><span></span><span></span><span></span></div>
    <div class="copy">© lumewear.example All Rights Reserved</div>
  </footer>
</main>
</body>
</html>
```